Webdesign for Non profit Diabetes education company

We are looking for a website design for our company.

We just created the company Glucose Guidance Circle

The concept for the company is to educate diabetics with resources that will help them manage their Diabetes. The list of advisers will be dietitians, podiatrist, diabetic educators, and fitness centers.

Please see attached logo. I like the logo to include an image that connects people together.

I've attached our logo, please use the colors in the design of the site.

Creativity is encouraged. Have fun with this project. We are looking for a professional site but not to corporate.

The page must be written in HTML 5 and be responsive built for mobile. You can use bootstrap, jquery, or angular JS.

Wordpress or wix will not be accepted.

The website will be hosted at www.glucoseguidancecircle.example

Requirements
Must have
• The page must be written in HTML 5 and be responsive built for mobile. You can use bootstrap, jquery, or angular JS.
• The landing page should include a splash page. Please incorporate the logo and the
Should not have
• Wordpress or wix will not be accepted.

```html
<!DOCTYPE html>
<html lang="en">
<head>
<meta charset="utf-8">
<title>Glucose Guidance Circle</title>
<link rel="stylesheet" href="https://fonts.googleapis.com/css2?family=Roboto:wght@300;400;500;700;900&display=swap">
<style>
:root{
  --pink:#ef5b8e;
  --pink-dark:#e14479;
  --blue:#5a7fc9;
  --blue-dark:#3f63b0;
  --ink:#2b2b33;
  --muted:#6f7180;
  --line:#dfe3ec;
  --footer:#1e1f24;
  --footer-deep:#141519;
  --white:#ffffff;
}
*{box-sizing:border-box;margin:0;padding:0}
html,body{width:1200px;height:3276px;overflow:hidden}
body{font-family:"Roboto",Arial,sans-serif;color:var(--ink);background:var(--white);position:relative}
.section{position:absolute;left:0;width:1200px}
.brand{display:flex;align-items:center;gap:10px}
.brand-mark{width:30px;height:30px;border-radius:50%;background:var(--pink)}
.brand-name{font-size:16px;font-weight:700;color:var(--blue-dark);width:150px;line-height:1.1}
/* header */
.site-header{top:0;height:88px;background:var(--white)}
.site-header .brand{position:absolute;left:90px;top:12px}
.contact-strip{position:absolute;left:430px;top:10px;display:flex;gap:36px;font-size:11px;color:var(--muted)}
.contact-strip .item{display:flex;gap:8px;align-items:center}
.contact-strip .ico{width:22px;height:22px;border-radius:50%;background:var(--blue);display:flex;align-items:center;justify-content:center}
.contact-strip b{display:block;color:var(--ink);font-size:11px}
.main-nav{position:absolute;left:320px;right:0;top:60px;height:28px;background:var(--pink);display:flex;gap:30px;padding-left:22px;align-items:center}
.main-nav a{color:var(--white);font-size:10px;font-weight:700;text-decoration:none;letter-spacing:.5px}
.main-nav a.active{background:var(--pink-dark);padding:9px 12px}
/* hero */
.hero{top:88px;height:564px;background:linear-gradient(115deg,#cfd6df 0%,#aab6c4 40%,#7f8fa3 75%,#6c7a8d 100%)}
.hero-card{position:absolute;left:200px;top:150px;width:420px;height:230px;background:var(--pink);padding:30px 32px;color:var(--white)}
.hero-card h1{font-size:36px;font-weight:700;line-height:1.1}
.hero-card .sub{font-size:15px;font-weight:700;margin-top:10px;text-decoration:underline}
.hero-copy{position:absolute;left:228px;top:406px;width:300px;font-size:11px;color:#3c3f4a;line-height:1.5}
.hero-actions{position:absolute;left:228px;top:486px;display:flex;gap:16px}
.btn{display:inline-block;font-size:11px;font-weight:700;padding:10px 18px;text-decoration:none;letter-spacing:.5px}
.btn-light{background:var(--white);color:var(--ink);border:1px solid var(--line)}
.btn-blue{background:var(--blue);color:var(--white)}
.btn-pink{background:var(--pink);color:var(--white)}
.hero-arrow{position:absolute;top:262px;width:40px;height:40px;border-radius:50%;background:rgba(30,30,40,.55);display:flex;align-items:center;justify-content:center}
/* headings */
.heading{text-align:center;font-size:28px;font-weight:700;color:var(--ink)}
.lead{text-align:center;font-size:12px;color:var(--muted);line-height:1.6}
.mission{top:652px;height:248px}
.mission .heading{margin-top:60px;font-size:26px}
.mission .rule,.facts .rule{width:760px;height:1px;background:var(--line);margin:14px auto 20px}
.mission .lead{width:760px;margin:0 auto;font-style:italic}
.facts{top:900px;height:300px}
.facts .heading{margin-top:60px}
.facts .lead{width:720px;margin:0 auto}
.stat-row{display:flex;width:760px;margin:24px auto 0;gap:4px}
.stat{flex:1;height:104px;background:var(--blue);color:var(--white);padding:14px 18px;position:relative}
.stat:nth-child(2){background:#4a6fbf}.stat:nth-child(3){background:var(--blue-dark)}
.stat h3{font-size:11px;font-weight:700;margin-top:22px}
.stat p{font-size:9px;line-height:1.35;opacity:.9}
.stat .more{font-size:9px;font-weight:700;position:absolute;bottom:10px}
.stat svg{position:absolute;top:12px;left:18px}
/* network */
.network{top:1232px;height:528px}
.network .panel{position:absolute;left:0;top:0;width:620px;height:528px;background:linear-gradient(90deg,#f46c9b,var(--pink))}
.network .photo{position:absolute;left:600px;top:0;width:600px;height:528px;background:linear-gradient(135deg,#e6e2df,#c9c3c0 60%,#b3aaa7)}
.network-text{position:absolute;left:200px;top:76px;width:330px;display:flex;flex-direction:column;align-items:flex-start}
.network-text h2{color:var(--white);font-size:26px;font-weight:700;line-height:1.2}
.network-text .copy{color:var(--white);font-size:11px;line-height:1.55;margin-top:22px;width:300px}
.network-text .btn{margin-top:40px}
.providers{position:absolute;left:550px;top:90px;width:380px;height:290px;background:rgba(255,255,255,.92);padding:24px 26px;display:grid;grid-template-columns:1fr 1fr;gap:14px 22px;align-content:start}
.providers h4{font-size:11px;color:var(--pink);font-weight:700}
.providers p{font-size:9px;color:var(--muted);line-height:1.4}
.providers .wide{grid-column:2}
/* government */
.programs{top:1760px;height:400px}
.programs .heading{width:700px;margin:70px auto 0;line-height:1.25;font-size:27px}
.program-row{display:flex;gap:20px;width:780px;margin:40px auto 0}
.program{flex:1;height:188px;border:1px solid var(--line);text-align:center;padding:20px 12px}
.program .ico{width:56px;height:56px;margin:0 auto 12px;border:2px solid var(--blue);border-radius:8px;display:flex;align-items:center;justify-content:center}
.program h4{font-size:11px;color:var(--blue-dark);font-weight:700}
.program p{font-size:9px;color:var(--muted);margin-top:8px;line-height:1.45}
/* signup */
.signup{top:2160px;height:288px;background:var(--blue)}
.signup .heading{color:var(--white);font-size:24px;margin-top:36px}
.signup-form{width:580px;margin:36px auto 0;display:grid;grid-template-columns:repeat(3,1fr);gap:12px}
.field{height:30px;background:var(--white);font-size:9px;color:#8a8d99;padding:10px 12px}
.signup-form .submit{background:var(--pink);color:var(--white);font-weight:700;font-size:10px;text-align:left;padding:10px 16px}
/* blog */
.blog{top:2448px;height:424px}
.blog .heading{margin-top:68px;font-size:26px}
.posts{display:flex;gap:36px;width:740px;margin:40px auto 0}
.post{flex:1;display:flex;gap:12px}
.post .photo{width:150px;height:220px;background:linear-gradient(160deg,#dfe4ea,#b8c2cf)}
.post .body{flex:1}
.post .tag{display:flex;gap:8px;background:var(--pink);color:var(--white);font-size:8px;font-weight:700;padding:7px 10px}
.post h4{font-size:10px;font-weight:700;margin-top:14px;line-height:1.4}
.post p{font-size:9px;color:var(--muted);margin-top:10px;line-height:1.5}
.post .more{font-size:9px;color:var(--pink);font-weight:700;margin-top:10px;display:block}
.dots{display:flex;gap:5px;justify-content:center;margin-top:30px}
.dots span{width:6px;height:6px;border-radius:50%;background:var(--ink)}
/* footer */
.site-footer{top:2872px;height:368px;background:var(--footer);color:#c9cbd3}
.site-footer .brand{position:absolute;left:110px;top:46px}
.site-footer .brand-name{color:var(--white)}
.foot-contact{position:absolute;left:110px;top:140px;font-size:10px;line-height:1.5}
.foot-contact .row{display:flex;gap:10px;margin-bottom:14px}
.foot-contact .ico{width:20px;height:20px;border-radius:50%;border:1px solid #5b5e6a;flex:none}
.foot-col h5,.newsletter h5{font-size:11px;font-weight:700;color:var(--white);margin-bottom:14px}
.quick{position:absolute;left:460px;top:60px;display:grid;grid-template-columns:150px 110px;gap:10px 0;font-size:10px}
.quick h5{grid-column:1/3;margin-bottom:4px}
.newsletter{position:absolute;left:780px;top:60px;width:250px}
.newsletter .grid{display:grid;grid-template-columns:1fr 1fr;gap:8px}
.newsletter .field{height:26px;padding:8px 10px}
.newsletter .full{grid-column:1/3}
.newsletter .send{grid-column:2;background:var(--blue);color:var(--white);font-weight:700;font-size:10px;text-align:center;padding:8px}
.bottom-bar{top:3240px;height:36px;background:var(--footer-deep);color:#9799a3;font-size:9px;display:flex;align-items:center;justify-content:space-between;padding:0 110px}
.social{display:flex;gap:8px}
.social span{width:16px;height:16px;border-radius:50%;background:#3a3c45}
</style>
</head>
<body>

<header class="section site-header">
  <div class="brand"><span class="brand-mark"></span><span class="brand-name">Glucose Guidance Circle</span></div>
  <div class="contact-strip">
    <div class="item"><span class="ico"><svg width="10" height="10" viewBox="0 0 10 10"><path d="M2 1l2 2-1 1.5a5 5 0 0 0 2.5 2.5L7 6l2 2-1.5 1.5C4 9 1 6 .5 2.5z" fill="#fff"/></svg></span><div><b>Call us</b>+1 (555) 013-2048</div></div>
    <div class="item"><span class="ico"><svg width="10" height="12" viewBox="0 0 10 12"><path d="M5 0a4 4 0 0 1 4 4c0 3-4 8-4 8S1 7 1 4a4 4 0 0 1 4-4z" fill="#fff"/><circle cx="5" cy="4" r="1.5" fill="#5a7fc9"/></svg></span><div><b>Location</b>1200 Sample Avenue, Suite 4</div></div>
    <div class="item"><span class="ico"><svg width="12" height="9" viewBox="0 0 12 9"><rect x=".5" y=".5" width="11" height="8" fill="none" stroke="#fff"/><path d="M.5.5L6 5l5.5-4.5" fill="none" stroke="#fff"/></svg></span><div><b>E-mail</b>hello@glucoseguidancecircle.example</div></div>
  </div>
  <nav class="main-nav">
    <a class="active" href="#">HOME</a><a href="#">FIND A HEALTHCARE PROVIDER</a><a href="#">JOIN OUR NETWORK</a><a href="#">NEWSLETTER</a><a href="#">BLOG</a>
  </nav>
</header>

<section class="section hero" role="img" aria-label="Photo of a person checking blood glucose with a testing pen">
  <div class="hero-card">
    <h1>Glucose Guidance Circle.</h1>
    <div class="sub">Glucose Guidance Circle.</div>
  </div>
  <p class="hero-copy">Diabetes occurs when your blood glucose, also called blood sugar, is too high. High blood glucose can cause health problems over time.</p>
  <div class="hero-actions"><a class="btn btn-light" href="#">READ MORE</a><a class="btn btn-blue" href="#">CONTACT US</a></div>
  <span class="hero-arrow" style="left:24px"><svg width="12" height="12" viewBox="0 0 12 12"><path d="M8 1L3 6l5 5" stroke="#fff" stroke-width="2" fill="none"/></svg></span>
  <span class="hero-arrow" style="right:24px"><svg width="12" height="12" viewBox="0 0 12 12"><path d="M4 1l5 5-5 5" stroke="#fff" stroke-width="2" fill="none"/></svg></span>
</section>

<section class="section mission">
  <h2 class="heading">Mission Statement</h2>
  <div class="rule"></div>
  <p class="lead">"At the Glucose Guidance Circle, our focus is to connect newly diagnosed and existing patients with diabetes on a network of available professionals who possess the knowledge to manage your diabetes"</p>
</section>

<section class="section facts">
  <h2 class="heading">Diabetes Facts and Statistics</h2>
  <div class="rule"></div>
  <p class="lead">Diabetes occurs when your blood glucose, also called blood sugar, is too high. High blood glucose can cause health problems over time. The most types of diabetes are type 1, type 2, and gestational.</p>
  <div class="stat-row">
    <div class="stat"><svg width="18" height="18" viewBox="0 0 18 18"><path d="M2 16h14M4 14V8M8 14V4M12 14V10" stroke="#fff" stroke-width="2"/></svg><h3>TOTAL</h3><p>An estimated 30.3 million people have diabetes, or 9.4% of the U.S. population.</p><span class="more">READ MORE</span></div>
    <div class="stat"><svg width="18" height="18" viewBox="0 0 18 18"><circle cx="9" cy="9" r="7" stroke="#fff" stroke-width="2" fill="none"/><path d="M5 9l3 3 5-6" stroke="#fff" stroke-width="2" fill="none"/></svg><h3>DIAGNOSED</h3><p>An estimated 23.1 million people have been diagnosed with diabetes in the country.</p><span class="more">READ MORE</span></div>
    <div class="stat"><svg width="18" height="18" viewBox="0 0 18 18"><path d="M9 1v16M1 9h16M3 3l12 12M15 3L3 15" stroke="#fff" stroke-width="1.6"/></svg><h3>UNDIAGNOSED</h3><p>An estimated 7.2 million adults ages 18 years or older are undiagnosed (23.8 percent).</p><span class="more">READ MORE</span></div>
  </div>
</section>

<section class="section network">
  <div class="panel"></div>
  <div class="photo" role="img" aria-label="Photo of a doctor consulting with a patient"></div>
  <div class="network-text">
    <h2>Our Network of Healthcare Providers Will Help You Manage Your Diabetes.</h2>
    <p class="copy">Lorem ipsum care with our trusted network of local providers and dietitians. All members are experts ready to share resources and guidance. Reach out to find the specialist who fits your needs and daily routine.</p>
    <a class="btn btn-blue" href="#">READ MORE</a>
  </div>
  <div class="providers">
    <div><h4>PODIATRIST</h4><p>A physician who specializes in the care of feet and ankles.</p></div>
    <div><h4>DIABETIC EDUCATOR</h4><p>A health professional who possesses knowledge of and experience in care.</p></div>
    <div><h4>ENDOCRINOLOGIST</h4><p>A physician who specializes in treating disorders of the endocrine system.</p></div>
    <div><h4>NUTRITIONISTS</h4><p>An expert in dietetics, which includes human nutrition and diets.</p></div>
    <div class="wide"><h4>PODIATRIST</h4><p>A doctor qualified to treat and keep feet and lower limbs healthy and active.</p></div>
  </div>
</section>

<section class="section programs">
  <h2 class="heading">Did You know that the Government has Setup Programs to Help Educate, Manage, and Prevent your Diabetes?</h2>
  <div class="program-row">
    <div class="program"><div class="ico"><svg width="26" height="26" viewBox="0 0 26 26"><circle cx="13" cy="8" r="5" fill="none" stroke="#5a7fc9" stroke-width="2"/><path d="M3 24c1-6 5-9 10-9s9 3 10 9" fill="none" stroke="#5a7fc9" stroke-width="2"/></svg></div><h4>PODIATRIST SERVICES</h4><p>A physician who specializes in treating disorders of the endocrine system.</p></div>
    <div class="program"><div class="ico"><svg width="26" height="26" viewBox="0 0 26 26"><rect x="4" y="3" width="18" height="20" fill="none" stroke="#5a7fc9" stroke-width="2"/><path d="M8 9h10M8 13h10M8 17h6" stroke="#5a7fc9" stroke-width="2"/></svg></div><h4>DIABETES EDUCATORS</h4><p>The purpose of this program is to help local families learn the knowledge.</p></div>
    <div class="program"><div class="ico"><svg width="26" height="26" viewBox="0 0 26 26"><circle cx="13" cy="14" r="9" fill="none" stroke="#5a7fc9" stroke-width="2"/><path d="M13 5c0-2 2-3 4-3" fill="none" stroke="#5a7fc9" stroke-width="2"/></svg></div><h4>NUTRITIONISTS</h4><p>Most often trained in care, this is an evidence based nutrition approach to eating.</p></div>
    <div class="program"><div class="ico"><svg width="26" height="26" viewBox="0 0 26 26"><path d="M13 3v20M3 13h20" stroke="#5a7fc9" stroke-width="3"/></svg></div><h4>PODIATRIST</h4><p>Podiatric services such as foot exams reduce diabetic foot ulcers and diseases.</p></div>
  </div>
</section>

<section class="section signup">
  <h2 class="heading">Healthcare Professional - Sign Up to be Part of Our Network</h2>
  <div class="signup-form">
    <div class="field">FIRST NAME</div><div class="field">LAST NAME</div><div class="field">PHONE</div>
    <div class="field">E-MAIL</div><div class="field">TITLE</div><div class="field">CITY</div>
    <div class="field" style="grid-column:2">ZIP CODE</div><div class="field submit">SUBMIT</div>
  </div>
</section>

<section class="section blog">
  <h2 class="heading">Our Latest Blog</h2>
  <div class="posts">
    <article class="post">
      <div class="photo" role="img" aria-label="Photo of an older couple reading together"></div>
      <div class="body"><div class="tag"><span>FEB 1, 2018</span><span>COMMENT</span></div><h4>LOREM IPSUM IS SIMPLY DUMMY TEXT OF THE PRINTING...</h4><p>Lorem ipsum is simply dummy text of the printing and typesetting industry. Lorem ipsum has been the standard text of the trade.</p><span class="more">READ MORE</span></div>
    </article>
    <article class="post">
      <div class="photo" role="img" aria-label="Photo of a glucose meter and test strip"></div>
      <div class="body"><div class="tag"><span>FEB 1, 2018</span><span>COMMENT</span></div><h4>LOREM IPSUM IS SIMPLY DUMMY TEXT OF THE PRINTING...</h4><p>Lorem ipsum is simply dummy text of the printing and typesetting industry. Lorem ipsum has been the standard text of the trade.</p><span class="more">READ MORE</span></div>
    </article>
  </div>
  <div class="dots"><span></span><span></span><span></span></div>
</section>

<footer class="section site-footer">
  <div class="brand"><span class="brand-mark"></span><span class="brand-name">Glucose Guidance Circle</span></div>
  <div class="foot-contact">
    <div class="row"><span class="ico"></span><div>CALL US<br>+1 (555) 013-2048</div></div>
    <div class="row"><span class="ico"></span><div>E-MAIL US<br>hello@glucoseguidancecircle.example</div></div>
    <div class="row"><span class="ico"></span><div>1200 Sample Avenue, Suite 4<br>Springfield, USA</div></div>
  </div>
  <div class="quick foot-col">
    <h5>QUICK LINKS</h5>
    <span>Home</span><span>Site Map</span>
    <span>Find a healthcare provider</span><span>Terms &amp; Conditions</span>
    <span>Join our network</span><span>Privacy Policy</span>
    <span>Newsletter</span><span>FAQ</span>
    <span>Blog</span><span></span>
  </div>
  <div class="newsletter">
    <h5>SIGN UP FOR OUR NEWSLETTER</h5>
    <div class="grid"><div class="field">First Name</div><div class="field">Last Name</div><div class="field full">E-mail</div><div class="send">SEND</div></div>
  </div>
</footer>
<div class="section bottom-bar"><span>© Glucose Guidance Circle 2018. All Rights Reserved</span><div class="social"><span></span><span></span><span></span></div></div>

</body>
</html>
```